Clark County Assessor Canditate

We need a billboard ad for a political candidate Tessa Harrow who is running for Clark County Assessor in an upcoming election. Needs to be simple and to the point to get the people to see the name "Tessa Harrow" and what to vote for "Clark County Assessor" in Las Vegas, NV. Also the billboard visibility is best in the top side of the sign, so the information should be most prominent in the top right, middle, left sides.The size of the billboard is 14 ft Height X 48 ft Wide Also needs some bright colors that are noticable from a freeway viewed billboard.Designers - I need to have "Paid for by Tessa Harrow for Clark County Assessor" on the sign
I have uploaded a few headshots you can work with to create a design. Thank you,

http://tessaharrow-vote.info/

Voters

Political

• Name, what I am voting for, and some image that represents Las Vegas and/or Nevada

```html
<!DOCTYPE html>
<html lang="en">
<head>
<meta charset="utf-8">
<title>Tessa Harrow for Clark County Assessor — Billboard</title>
<link rel="stylesheet" href="https://fonts.googleapis.com/css2?family=Open+Sans:wdth,wght@75..100,400..800&display=swap">
<style>
  :root {
    --red: #e10000;
    --blue: #0b5092;
    --paper: #f1f1f1;
    --white: #ffffff;
    --hair: #d9b77a;
    --jacket: #1f1f22;
    --skin: #e9c3a8;
  }
  * { margin: 0; padding: 0; box-sizing: border-box; }
  html, body {
    width: 1200px;
    height: 407px;
    overflow: hidden;
    background: var(--paper);
  }
  .billboard {
    position: relative;
    width: 1200px;
    height: 407px;
    overflow: hidden;
    background: linear-gradient(90deg, #e9e9e9 0%, var(--paper) 40%, var(--white) 100%);
    font-family: "Open Sans", Arial, sans-serif;
    color: var(--white);
  }
  .bands {
    position: absolute;
    inset: 0;
    width: 1200px;
    height: 407px;
  }
  .headshot {
    position: absolute;
    left: 66px;
    top: 14px;
    width: 344px;
    height: 393px;
    border-radius: 150px 150px 0 0;
    background:
      radial-gradient(ellipse 30% 26% at 50% 34%, var(--skin) 0%, var(--skin) 60%, rgba(233,195,168,0) 100%),
      linear-gradient(180deg, var(--hair) 0%, var(--hair) 62%, var(--jacket) 78%, var(--jacket) 100%);
  }
  .vote-label {
    position: absolute;
    left: 402px;
    top: 14px;
    font-size: 74px;
    font-weight: 800;
    font-stretch: 82%;
    line-height: 1;
    letter-spacing: 0.5px;
  }
  .candidate-name {
    position: absolute;
    right: 73px;
    top: 108px;
    font-size: 128px;
    font-weight: 800;
    font-stretch: 80%;
    line-height: 1;
    letter-spacing: -0.5px;
    white-space: nowrap;
  }
  .office {
    position: absolute;
    right: 73px;
    top: 240px;
    text-align: right;
    font-weight: 800;
    line-height: 1;
    white-space: nowrap;
  }
  .office-for {
    display: block;
    font-size: 40px;
    font-stretch: 85%;
  }
  .office-title {
    display: block;
    margin-top: 6px;
    font-size: 63px;
    font-stretch: 84%;
    letter-spacing: 0.3px;
  }
  .disclaimer {
    position: absolute;
    right: 73px;
    top: 355px;
    font-size: 14px;
    font-weight: 400;
    white-space: nowrap;
  }
  .disclaimer strong { font-weight: 700; }
</style>
</head>
<body>
  <main class="billboard">
    <svg class="bands" viewBox="0 0 1200 407" aria-hidden="true">
      <polygon class="band-red" points="426,0 1200,0 1200,227 350,227" fill="var(--red)"/>
      <rect class="band-blue" x="350" y="227" width="850" height="180" fill="var(--blue)"/>
      <polygon class="vote-tab" points="373,21 602,21 575,104 335,104" fill="var(--blue)"/>
    </svg>

    <div class="headshot" role="img" aria-label="Headshot of candidate Tessa Harrow"></div>

    <div class="vote-label">VOTE</div>
    <h1 class="candidate-name">Tessa Harrow</h1>
    <p class="office">
      <span class="office-for">FOR</span>
      <span class="office-title">CLARK COUNTY ASSESSOR</span>
    </p>
    <p class="disclaimer">Paid for by <strong>Tessa Harrow</strong> for Clark County Assessor</p>
  </main>
</body>
</html>
```